Retail Jewelry Business Card Design Project

We are in need of a new business card design for a retail jewelry store. This store is in the business of fine jewelry including but not specific to bridal jewelry, diamonds, designer jewelry and watches.

This store has been in business for 20 years but continues to strive for a modern professional appeal. The main colors use for this business are a royal blue, white and silver.

Target Market(s)

Target market is ages 18-50

Industry/Entity Type

Jewelry

Requirements
Must have
• Sales Person Name
Sales Person Email Address

Store Address
Store Phone
Website

Standard business card size. No odd shapes or sizes.
Nice to have
• Overall modern feel for card.

We have thought that a design with a nice feature of the logo on the back of the card would be nice but open to ideas.
Should not have
• No specific images of jewelry should be used.

```html
<!DOCTYPE html>
<html lang="en">
<head>
<meta charset="utf-8">
<title>Adrian Kent Fine Jewelry – Business Cards</title>
<link rel="stylesheet" href="https://fonts.googleapis.com/css2?family=Arimo:wght@400;700&family=Tinos:wght@400;700&display=swap">
<style>
  :root {
    --royal-blue: #3a3a88;
    --royal-blue-deep: #2a2a6e;
    --royal-blue-soft: #4a4a9a;
    --card-white: #f7f7f8;
    --silver: #c9cad3;
    --ink-light: #ffffff;
    --backdrop: #2b2d30;
  }
  * { box-sizing: border-box; margin: 0; padding: 0; }
  html, body { width: 800px; height: 1200px; overflow: hidden; }
  body {
    background: var(--backdrop);
    display: flex;
    flex-direction: column;
    align-items: center;
    justify-content: space-around;
    padding: 90px 0;
  }
  .card {
    width: 640px;
    height: 366px;
    position: relative;
    overflow: hidden;
    box-shadow: 0 10px 30px rgba(0,0,0,0.45);
  }

  /* Brand name */
  .brand {
    text-align: center;
    font-family: "Tinos", serif;
    font-weight: 700;
    line-height: 1;
  }
  .brand__name { display: block; font-size: 50px; letter-spacing: 0.5px; }
  .brand__tagline { display: block; font-size: 18px; letter-spacing: 2px; margin-top: 8px; }

  /* Front */
  .card--front { background: var(--card-white); }
  .card--front .brand {
    position: absolute; top: 48px; left: 0; right: 0;
    color: var(--royal-blue);
  }
  .contact-band {
    position: absolute;
    left: 0; right: 0; top: 164px; height: 92px;
    background: var(--royal-blue);
    color: var(--ink-light);
    display: flex;
    align-items: center;
  }
  .contact-band__person { width: 322px; padding-left: 52px; }
  .contact-band__name {
    font-family: "Arimo", sans-serif; font-weight: 700; font-size: 18px;
  }
  .contact-band__email {
    font-family: "Tinos", serif; font-size: 12px; margin-top: 8px;
  }
  .contact-band__divider {
    width: 1px; height: 66px; background: var(--silver); opacity: 0.8;
  }
  .contact-band__details { padding-left: 14px; font-family: "Tinos", serif; font-size: 11.5px; }
  .detail { display: flex; align-items: flex-start; gap: 10px; line-height: 1.3; }
  .detail + .detail { margin-top: 10px; }
  .detail svg { flex: none; width: 11px; height: 13px; margin-top: 1px; fill: var(--ink-light); }
  .website {
    position: absolute; left: 0; right: 0; top: 276px;
    text-align: center;
    font-family: "Arimo", sans-serif; font-size: 17px;
    color: var(--royal-blue);
  }

  /* Back */
  .card--back {
    background: radial-gradient(ellipse at 45% 40%, var(--royal-blue-soft) 0%, var(--royal-blue) 45%, var(--royal-blue-deep) 100%);
    display: flex; align-items: center; justify-content: center;
  }
  .card--back .brand { color: var(--ink-light); }
</style>
</head>
<body>

<section class="card card--front" aria-label="Business card front">
  <div class="brand">
    <span class="brand__name">Adrian Kent</span>
    <span class="brand__tagline">FINE JEWELRY</span>
  </div>

  <div class="contact-band">
    <div class="contact-band__person">
      <div class="contact-band__name">Adrian Kent Halloway</div>
      <div class="contact-band__email">adrian@adriankentjewelry.com</div>
    </div>
    <div class="contact-band__divider"></div>
    <div class="contact-band__details">
      <div class="detail">
        <svg viewBox="0 0 24 24" aria-hidden="true"><path d="M6.6 10.8a15.1 15.1 0 0 0 6.6 6.6l2.2-2.2a1 1 0 0 1 1-.25 11.4 11.4 0 0 0 3.6.57 1 1 0 0 1 1 1V20a1 1 0 0 1-1 1A17 17 0 0 1 3 4a1 1 0 0 1 1-1h3.5a1 1 0 0 1 1 1c0 1.25.2 2.45.57 3.57a1 1 0 0 1-.25 1z"/></svg>
        <span>(555) 014-2290</span>
      </div>
      <div class="detail">
        <svg viewBox="0 0 24 24" aria-hidden="true"><path d="M12 2a7 7 0 0 0-7 7c0 5.25 7 13 7 13s7-7.75 7-13a7 7 0 0 0-7-7zm0 9.5A2.5 2.5 0 1 1 12 6.5a2.5 2.5 0 0 1 0 5z"/></svg>
        <span>2207 Marlow Avenue<br>Bayford, FL 32000</span>
      </div>
    </div>
  </div>

  <div class="website">www.adriankentjewelry.com</div>
</section>

<section class="card card--back" aria-label="Business card back">
  <div class="brand">
    <span class="brand__name">Adrian Kent</span>
    <span class="brand__tagline">FINE JEWELRY</span>
  </div>
</section>

</body>
</html>
```